New email newsletter banner needed

Financial services firm need a new banner for a newsletter banner. The old one attached.... Size is 4cm x 16cm and should read "Looking for Options".

Base colors can be Pantone colors 281,644,425,1805,405 and any gradient of those.

Font should be Arial MT

Please note the firm mentioned in the old banner no longer applies

Financial

• images of people, multiple images

```html
<!DOCTYPE html>
<html lang="en">
<head>
<meta charset="utf-8">
<title>Looking for Options – Newsletter Banners</title>
<link rel="preconnect" href="https://fonts.googleapis.com">
<link href="https://fonts.googleapis.com/css2?family=Arvo:wght@700&display=swap" rel="stylesheet">
<style>
  :root {
    --page: #ffffff;
    --sky-light: #9db7d8;
    --sky-mid: #6488bd;
    --navy: #2a4e96;
    --navy-deep: #132f6c;
    --taupe: #645d57;
    --red-glow: #e56a66;
    --red: #c1393b;
    --red-deep: #8f1f24;
    --cream: #fdfbe6;
    --ink: #4a403b;
    --white: #ffffff;
  }
  html, body {
    margin: 0;
    padding: 0;
    width: 1200px;
    height: 739px;
    overflow: hidden;
    background: var(--page);
  }
  .banners {
    display: block;
    width: 1200px;
    height: 739px;
  }
  .headline {
    font-family: "Arvo", "Rockwell", serif;
    font-weight: 700;
  }
  .headline--light {
    fill: var(--white);
    filter: drop-shadow(3px 4px 2px rgba(0, 0, 0, 0.75));
  }
  .headline--outlined {
    fill: var(--cream);
    stroke: var(--ink);
    stroke-width: 9px;
    stroke-linejoin: round;
    paint-order: stroke;
  }
</style>
</head>
<body>
<svg class="banners" viewBox="0 0 1200 739" xmlns="http://www.w3.org/2000/svg">
  <defs>
    <linearGradient id="sky" x1="0" y1="0" x2="0" y2="1">
      <stop offset="0" stop-color="var(--sky-light)"/>
      <stop offset="1" stop-color="var(--sky-mid)"/>
    </linearGradient>
    <linearGradient id="navy" x1="0" y1="0" x2="0" y2="1">
      <stop offset="0" stop-color="var(--navy)"/>
      <stop offset="1" stop-color="var(--navy-deep)"/>
    </linearGradient>
    <radialGradient id="redGlow" cx="0.35" cy="0.1" r="0.8">
      <stop offset="0" stop-color="var(--red-glow)"/>
      <stop offset="0.6" stop-color="var(--red)"/>
      <stop offset="1" stop-color="var(--red-deep)"/>
    </radialGradient>
    <linearGradient id="stripeFade" x1="0" y1="0" x2="1" y2="0">
      <stop offset="0" stop-color="var(--cream)"/>
      <stop offset="0.6" stop-color="var(--cream)"/>
      <stop offset="1" stop-color="var(--cream)" stop-opacity="0"/>
    </linearGradient>
    <clipPath id="blueShape"><rect x="53" y="64" width="1092" height="276" rx="12"/></clipPath>
    <clipPath id="redShape"><rect x="53" y="409" width="1092" height="281" rx="10"/></clipPath>
  </defs>

  <g class="banner banner--blue" clip-path="url(#blueShape)">
    <rect x="53" y="64" width="1092" height="276" fill="var(--taupe)"/>
    <path d="M53 192 H1145 V265 Q600 370 53 265 Z" fill="url(#navy)"/>
    <rect x="53" y="64" width="1092" height="128" fill="url(#sky)"/>
    <text class="headline headline--light" x="600" y="160" font-size="96" text-anchor="middle">Looking for</text>
    <text class="headline headline--light" x="600" y="270" font-size="96" text-anchor="middle">Options</text>
  </g>

  <g class="banner banner--red" clip-path="url(#redShape)">
    <rect x="53" y="409" width="1092" height="281" fill="url(#redGlow)"/>
    <rect class="stripe" x="53" y="450" width="700" height="74" fill="url(#stripeFade)"/>
    <rect class="stripe" x="53" y="556" width="700" height="79" fill="url(#stripeFade)"/>
    <text class="headline headline--outlined" x="585" y="520" font-size="86">Looking</text>
    <text class="headline headline--outlined" x="585" y="622" font-size="86">for Options</text>
  </g>
</svg>
</body>
</html>
```